Professional Speaker needs a Business Card Design

I am a Professional Speaker and I need a design for my business cards. I would like for it to look sleek and professional but not too busy or cluttered. The colors I need are a bright blue, middle level gray and white. I also want a picture on both the front and back of the card. I have somewhat of a design that I created but it's something very basic. I was having an issue with submitting my images to Kelmo Press because they weren't able to get me the exact colors I wanted. I would like to stick with something similar to what I came up with but am open to viewing your ideas.
Updates
Project Deadline Extended Reason: I've only received designs from a few designers. I would like to see some more options before I make my final decision. Added Thursday, January 08, 2015
Industry/Entity Type
Business
Contact Information for Business Card
Please refer to word document attached. It should be file 5 and that contains all of the details I need on my card. Also please be sure and use my Logo that is attached. The file is named logo front.
Look and feel

```html
<!DOCTYPE html>
<html lang="en">
<head>
<meta charset="utf-8">
<title>Darnell Brooks – Business Card</title>
<link rel="stylesheet" href="https://fonts.googleapis.com/css2?family=Fauna+One&family=Lato:wght@300;400&family=Sniglet:wght@400;800&family=Cormorant+Garamond:wght@400&display=swap">
<style>
  :root {
    --navy: #1c2b5a;
    --blue: #3a55b5;
    --sky: #4aa3df;
    --gray: #b4b4b4;
    --white: #ffffff;
    --bg: #d9d9d9;
    --photo-light: #c9ced8;
    --photo-dark: #6e7480;
  }
  * { margin: 0; padding: 0; box-sizing: border-box; }
  html, body { width: 1200px; height: 900px; overflow: hidden; }
  body {
    background: radial-gradient(circle at 50% 40%, #ededed, var(--bg));
    position: relative;
    font-family: "Fauna One", serif;
  }
  .card {
    position: absolute;
    left: 170px;
    width: 860px;
    height: 390px;
    background: var(--white);
    border: 8px solid var(--navy);
    box-shadow: 0 6px 16px rgba(0,0,0,0.25);
    overflow: hidden;
  }
  .card--front { top: 40px; }
  .card--back { top: 470px; }

  /* Front */
  .front__band {
    position: absolute; left: 0; right: 0; bottom: 14px; height: 150px;
    background: var(--navy);
  }
  .front__band-rise {
    position: absolute; right: 0; bottom: 150px; width: 230px; height: 60px;
    background: var(--navy);
  }
  .front__brand {
    position: absolute; left: 200px; top: 26px;
    display: flex; align-items: center; gap: 12px;
  }
  .front__brand-mark { width: 44px; height: 44px; background: var(--blue); }
  .front__brand-name { font-size: 30px; color: var(--blue); }
  .front__title {
    position: absolute; left: 120px; top: 100px; width: 420px;
    text-align: center; font-family: "Lato", sans-serif;
    font-size: 26px; line-height: 1.2; color: var(--navy);
  }
  .front__photo {
    position: absolute; right: 60px; top: 14px; width: 150px; height: 330px;
    background: linear-gradient(180deg, var(--photo-light) 0 45%, var(--photo-dark) 45% 100%);
    border-radius: 56px 56px 10px 10px;
  }
  .socials {
    position: absolute; left: 30px; bottom: 92px;
    display: flex; gap: 18px; color: var(--white); font-size: 13px;
    list-style: none;
  }
  .social { display: flex; align-items: center; gap: 7px; white-space: nowrap; }
  .social__dot { width: 26px; height: 26px; border-radius: 50%; background: var(--white); flex: none; }
  .contact {
    position: absolute; left: 30px; bottom: 34px;
    color: var(--white); font-size: 13px; display: flex; gap: 12px;
    white-space: nowrap;
  }
  .contact__label { color: var(--sky); }

  /* Back */
  .back__photo-accent {
    position: absolute; left: 60px; top: 50px; width: 240px; height: 140px;
    background: var(--sky); transform: rotate(-8deg);
  }
  .back__photo-frame {
    position: absolute; left: 70px; top: 56px; width: 240px; height: 140px;
    background: var(--navy); transform: rotate(4deg);
  }
  .back__photo {
    position: absolute; left: 76px; top: 52px; width: 240px; height: 146px;
    background: linear-gradient(135deg, #e6e8ee, #9aa2b0);
    border: 3px solid var(--white);
  }
  .greeting {
    position: absolute; left: 345px; top: 64px;
    font-family: "Sniglet", sans-serif; font-weight: 400; color: var(--navy); line-height: 1;
  }
  .greeting__hi { font-size: 30px; }
  .greeting__name { font-size: 48px; font-weight: 800; }
  .roles {
    position: absolute; left: 0; right: 0; top: 210px; height: 66px;
    background: var(--navy); color: var(--white);
    font-family: "Lato", sans-serif; font-weight: 300;
    font-size: 34px; letter-spacing: 3px;
    display: flex; align-items: center; justify-content: center;
  }
  .motto {
    position: absolute; left: 0; right: 0; top: 282px;
    text-align: center; font-family: "Cormorant Garamond", serif;
    font-size: 78px; line-height: 1;
  }
  .motto__love, .motto__life { color: var(--blue); }
  .motto__live { color: var(--gray); }
  .ornament {
    position: absolute; width: 44px; height: 44px; background: var(--blue);
    transform: rotate(45deg);
  }
  .ornament--left { left: 40px; top: 316px; }
  .ornament--right { right: 40px; top: 316px; }
</style>
</head>
<body>
  <section class="card card--front">
    <div class="front__band-rise"></div>
    <div class="front__band"></div>
    <div class="front__brand">
      <span class="front__brand-mark"></span>
      <span class="front__brand-name">Darnell Brooks</span>
    </div>
    <p class="front__title">CEO Brooks Unlimited<br>www.darnellbrooksnow.com</p>
    <div class="front__photo" role="img" aria-label="Full-length photo of the speaker standing"></div>
    <ul class="socials">
      <li class="social"><span class="social__dot"></span>Darnell Brooks</li>
      <li class="social"><span class="social__dot"></span>D.Brooks85</li>
      <li class="social"><span class="social__dot"></span>DarnellBrooks85</li>
      <li class="social"><span class="social__dot"></span>Darnell Brooks</li>
    </ul>
    <p class="contact">
      <span>For Requests Contact:</span>
      <span><span class="contact__label">Email:</span> info@darnellbrooksnow.com</span>
      <span><span class="contact__label">Phone:</span> 555-014-2290</span>
    </p>
  </section>

  <section class="card card--back">
    <div class="back__photo-accent"></div>
    <div class="back__photo-frame"></div>
    <div class="back__photo" role="img" aria-label="Photo of the speaker holding a microphone"></div>
    <h1 class="greeting">
      <span class="greeting__hi">Hi i am</span><br>
      <span class="greeting__name">darnell brooks</span>
    </h1>
    <div class="roles">SPEAKER - AUTHOR - COACH</div>
    <p class="motto"><span class="motto__love">Love.</span> <span class="motto__live">Live.</span> <span class="motto__life">Life.</span></p>
    <div class="ornament ornament--left" role="img" aria-label="Decorative diamond ornament"></div>
    <div class="ornament ornament--right" role="img" aria-label="Decorative diamond ornament"></div>
  </section>
</body>
</html>
```